Simple Website Design for Law Office

I need a website design for our law office (Law Offices of Marcus Trell) that is extremely simple, only including a landing page and perhaps a contact page (parallax scrolling).

Website should look similar to this one (template): https://www.quorvabellwith.com/

Design should be modern, simple, and inviting. There are a few assets like logo, stock photos/icons we would like added as well, and some language and contact info, but very basic stuff.

The name of the company is: Law Offices of Marcus Trell

Target Market(s)

B2B corporate clients, users from Canada, UK, East Asia, and all potential users with immigration needs

Coding

Number of Pages Required

2 page

Colors

Designer to choose colors to be used in the design.

Requirements
Must have
• Landing page, Contact Page
• Simple, elegant design with minimalist font
Nice to have
• Parallax scrolling, so one page and can scroll to contact us segment

```html
<!DOCTYPE html>
<html lang="en">
<head>
<meta charset="UTF-8">
<title>Law Offices of Marcus Trell</title>
<link href="https://fonts.googleapis.com/css2?family=Lato:wght@700&family=Montserrat:wght@400;600;700&display=swap" rel="stylesheet">
<style>
  :root {
    --white: #ffffff;
    --sky-light: #d3dde8;
    --sky-mid: #8fa2b8;
    --tower-dark: #1c2430;
    --tower-deep: #10151d;
    --button-fill: #141a22;
    --button-edge: #0b0f15;
  }
  * { margin: 0; padding: 0; box-sizing: border-box; }
  html, body { width: 1200px; height: 614px; overflow: hidden; }
  body { font-family: "Montserrat", sans-serif; color: var(--white); }

  .hero {
    position: relative;
    width: 1200px;
    height: 614px;
    overflow: hidden;
  }
  .hero-backdrop {
    position: absolute;
    inset: 0;
    background:
      radial-gradient(ellipse 55% 40% at 50% 10%, rgba(230,236,243,0.85), rgba(230,236,243,0) 70%),
      radial-gradient(ellipse 30% 60% at 95% 40%, rgba(120,140,165,0.7), rgba(120,140,165,0) 70%),
      linear-gradient(180deg, var(--sky-light) 0%, var(--sky-mid) 22%, var(--tower-dark) 55%, var(--tower-deep) 100%);
  }

  .brand {
    position: absolute;
    left: 161px;
    top: 68px;
    width: 170px;
    font-family: "Montserrat", sans-serif;
    font-weight: 600;
    font-size: 17px;
    line-height: 22px;
    letter-spacing: -0.3px;
    text-transform: uppercase;
    color: var(--white);
  }

  .main-nav {
    position: absolute;
    top: 67px;
    left: 586px;
    display: flex;
    gap: 0;
  }
  .main-nav a {
    font-size: 15px;
    font-weight: 400;
    color: var(--white);
    text-decoration: none;
    text-transform: uppercase;
    letter-spacing: 0.2px;
  }
  .main-nav a + a { margin-left: 32px; }

  .welcome-frame {
    position: absolute;
    left: 207px;
    top: 168px;
    width: 787px;
    height: 344px;
    border: 2px solid var(--white);
    text-align: center;
  }
  .welcome-title {
    margin-top: 40px;
    font-family: "Lato", sans-serif;
    font-weight: 700;
    font-size: 36px;
    line-height: 46px;
    text-transform: uppercase;
    text-shadow: 0 2px 8px rgba(0,0,0,0.55);
  }
  .welcome-title .initial { font-size: 46px; }
  .welcome-lede {
    margin-top: 44px;
    font-size: 14px;
    line-height: 19px;
  }
  .contact-button {
    position: absolute;
    left: 317px;
    top: 290px;
    width: 149px;
    height: 37px;
    border-radius: 19px;
    background: var(--button-fill);
    border: 1px solid var(--button-edge);
    color: var(--white);
    font-size: 10px;
    font-weight: 700;
    line-height: 35px;
    text-decoration: none;
    text-transform: uppercase;
  }
</style>
</head>
<body>
  <header class="hero">
    <div class="hero-backdrop" role="img" aria-label="Upward view of glass office towers against a pale cloudy sky"></div>

    <div class="brand">Law Offices of Marcus Trell</div>

    <nav class="main-nav">
      <a href="#">Home</a>
      <a href="#">About Us</a>
      <a href="#">Contact</a>
      <a href="#">Location</a>
    </nav>

    <section class="welcome-frame">
      <h1 class="welcome-title"><span class="initial">W</span>elcome to<br>Law Offices of Marcus Trell</h1>
      <p class="welcome-lede">Lorem ipsum dolor sit amet, consectetur adipisicing elit,<br>sed do eiusmod tempor.</p>
      <a class="contact-button" href="#">Contact Us</a>
    </section>
  </header>
</body>
</html>
```